Operator Qualification Testing Flyer

I have a 8x10 basic flyer that I created usin InDesign for one of our services our company provides. I would like to see more options for the layout and general design of the flyer. This flyer will be used as a template for the other services we provide. I will include the InDesign Folder with all the logos and images. Please feel free to use any logo design within the folder and you can change the font and/or colors as needed. I would like the final output in a Indesign package folder to be used in InDesign 2021

Target Market(s)

Business to Business marketing in the Oil and Gas industry

Font styles to use
Sans Serif

Colors
85cae6
85acd3
3377b5
0355a3
0792cd
ffffff
cedeed

Requirements
Must have
• I included/attached a couple of brochures styles that I do like.

```html
<!DOCTYPE html>
<html lang="en">
<head>
<meta charset="utf-8">
<title>Pipeline OQ Testing Flyer</title>
<link href="https://fonts.googleapis.com/css2?family=Open+Sans:wght@400;600;700&family=Roboto:wght@900&display=swap" rel="stylesheet">
<style>
  :root {
    --sky: #a8cfe8;
    --teal: #2a7d94;
    --teal-dark: #1f6679;
    --heading: #1b8fca;
    --body-text: #3a3f44;
    --paper: #ffffff;
    --paper-shade: #e6e7e9;
    --backdrop: #c9c9cb;
    --sign: #e8b21c;
    --white: #ffffff;
  }
  * { box-sizing: border-box; margin: 0; padding: 0; }
  html, body { width: 1200px; height: 960px; overflow: hidden; }
  body {
    background: var(--backdrop);
    font-family: "Open Sans", Arial, sans-serif;
    position: relative;
  }
  .flyer {
    position: absolute;
    left: 240px; top: 30px;
    width: 720px; height: 900px;
    background: linear-gradient(180deg, var(--paper) 0%, var(--paper) 65%, var(--paper-shade) 100%);
    overflow: hidden;
    box-shadow: 0 6px 20px rgba(0,0,0,.18);
  }
  .header-shape { position: absolute; left: 0; top: 0; width: 720px; height: 180px; }
  .brand {
    position: absolute; left: 40px; top: 40px;
    display: flex; align-items: center; gap: 12px;
  }
  .brand-dot { width: 40px; height: 40px; border-radius: 50%; background: var(--teal); }
  .brand-name { font-size: 24px; font-weight: 400; color: var(--white); }
  .contact {
    position: absolute; top: 72px;
    display: flex; flex-direction: column; align-items: center; gap: 6px;
    font-size: 11px; color: var(--body-text);
  }
  .contact-phone { left: 448px; }
  .contact-email { left: 560px; }
  .contact-icon { width: 18px; height: 18px; }
  .teal-band {
    position: absolute; left: 0; top: 280px; width: 720px; height: 200px;
    background: var(--teal);
  }
  .site-photo {
    position: absolute; left: 44px; top: 168px; width: 632px; height: 312px;
    background: linear-gradient(135deg, #9a8a78 0%, #b3a592 45%, #7c9a8f 70%, #8e8070 100%);
  }
  .title-banner {
    position: absolute; left: 70px; top: 192px; width: 600px; height: 72px;
    background: rgba(31,102,121,.72);
    display: flex; align-items: center; justify-content: center;
  }
  .title {
    font-family: "Roboto", Arial, sans-serif; font-weight: 900;
    font-size: 44px; letter-spacing: 1px; color: var(--white);
    text-shadow: 2px 2px 3px rgba(0,0,0,.5);
  }
  .warning-sign {
    position: absolute; left: 566px; top: 420px; width: 112px; height: 112px;
    border-radius: 50%; background: var(--sign); border: 4px solid #222;
  }
  .section-heading {
    color: var(--heading); font-weight: 700; font-size: 19px; line-height: 1.2;
  }
  .section-text {
    color: var(--body-text); font-size: 11px; line-height: 1.6;
  }
  .intro { position: absolute; left: 50px; top: 512px; width: 630px; }
  .intro .section-heading { margin-bottom: 8px; }
  .covered { position: absolute; left: 40px; top: 640px; width: 165px; }
  .covered .section-heading { margin-bottom: 14px; }
  .provide { position: absolute; left: 232px; top: 664px; width: 450px; }
  .provide .section-heading { margin-bottom: 12px; }
  .provide .section-text + .section-text { margin-top: 10px; }
</style>
</head>
<body>
  <article class="flyer">
    <svg class="header-shape" viewBox="0 0 720 180" aria-hidden="true">
      <polygon points="0,0 410,0 470,180 0,180" fill="var(--sky)"/>
    </svg>

    <div class="brand">
      <span class="brand-dot"></span>
      <span class="brand-name">Meridian Fieldworks Inc.</span>
    </div>

    <div class="contact contact-phone">
      <svg class="contact-icon" viewBox="0 0 18 18" aria-hidden="true">
        <circle cx="9" cy="9" r="9" fill="var(--teal)"/>
        <path d="M6.2 4.8l1.6 1.8-.8 1.2c.6 1.2 1.4 2 2.6 2.6l1.2-.8 1.8 1.6-.9 1.5c-3.1-.4-5.9-3.2-6.3-6.3z" fill="var(--white)"/>
      </svg>
      <span>406-555-0148</span>
    </div>
    <div class="contact contact-email">
      <svg class="contact-icon" viewBox="0 0 18 18" aria-hidden="true">
        <circle cx="9" cy="9" r="9" fill="var(--teal)"/>
        <rect x="4.5" y="6" width="9" height="6.5" rx="1" fill="var(--white)"/>
        <path d="M4.8 6.4L9 9.6l4.2-3.2" stroke="var(--teal)" stroke-width="1" fill="none"/>
      </svg>
      <span>dana@meridianfield.co</span>
    </div>

    <div class="teal-band"></div>
    <div class="site-photo" role="img" aria-label="Aerial photo of an excavator beside an open trench with green pipelines and crew"></div>
    <div class="title-banner"><h1 class="title">PIPELINE OQ TESTING</h1></div>
    <div class="warning-sign" role="img" aria-label="Round yellow petroleum pipeline warning marker"></div>

    <section class="intro">
      <h2 class="section-heading">What Is Operator Qualification?</h2>
      <p class="section-text">Operator Qualifications (OQ) for DOT Oil/Gas Pipelines are requirements set by Department of Transportation (DOT) and Pipeline and Hazardous Materials Safety Administration (PHMSA). To assure safety in the transport of hazardous gases and liquids in the nation's pipelines, pipeline operators who perform covered tasks must be qualified. Qualified means that an individual has been evaluated and can perform assigned covered tasks and recognize and react to abnormal operating conditions.</p>
    </section>

    <section class="covered">
      <h2 class="section-heading">What Are Covered Tasks?</h2>
      <p class="section-text">Covered tasks are defined in an operator's written plan which defines specific job functions or activities personnel are qualified to perform on a pipeline facility.</p>
    </section>

    <section class="provide">
      <h2 class="section-heading">What We Provide</h2>
      <p class="section-text">Meridian Fieldworks Inc. utilizes CSC pipeline program to administer OQ assessment testing on 127 covered tasks</p>
      <p class="section-text">Upon completion of OQ testing the information is first transferred to CSC's Registry System and automatically uploaded to SafeVendor.</p>
      <p class="section-text">In addition to the benefits provided by SafeVendor's database, the CSC Registry System houses all the completion information allowing candidates to share their training information and employers to verify successful covered task and level completions.</p>
    </section>
  </article>
</body>
</html>
```